Under Birch Light

I need a book cover showing a girl with long dark hair, preferably in a long dress, it needs the large oak tree in it somewhere in background "Under Birch light"

This is an adult book, of romance and adventure, the girl on the cover is a
teenage girl of 20, years of age, the book is to be a print 5x8 about 200
pages

Target Market(s)

Personal use

Industry/Entity Type

Hair

Colors
9bcb3c
fbed22
add136
fbee3f

Requirements
Must have
• the girl and the tree

```html
<!DOCTYPE html>
<html lang="en">
<head>
<meta charset="utf-8">
<title>Under Birch Light — Book Cover</title>
<link rel="stylesheet" href="https://fonts.googleapis.com/css2?family=Playfair+Display:ital,wght@0,400;0,700;1,400;1,700&display=swap">
<style>
  :root {
    --spine-red: #8b1a36;
    --title-blue: #93d3ea;
    --title-white: #f2f4ee;
    --text-cream: #f6f1e4;
    --forest-deep: #0f2419;
    --forest-mid: #27492c;
    --forest-light: #4f7a35;
    --box-white: #ffffff;
  }
  html, body {
    margin: 0;
    padding: 0;
    width: 1200px;
    height: 916px;
    overflow: hidden;
    background: #ffffff;
  }
  .cover-wrap {
    position: relative;
    width: 1200px;
    height: 916px;
    overflow: hidden;
    font-family: "Playfair Display", Georgia, serif;
  }
  .back-photo {
    position: absolute;
    left: 0; top: 0;
    width: 573px; height: 916px;
    background:
      radial-gradient(ellipse at 20% 75%, rgba(110,150,60,0.55), transparent 55%),
      radial-gradient(ellipse at 80% 20%, rgba(60,100,50,0.5), transparent 60%),
      linear-gradient(160deg, var(--forest-deep) 0%, var(--forest-mid) 45%, var(--forest-light) 80%, var(--forest-deep) 100%);
  }
  .front-photo {
    position: absolute;
    left: 627px; top: 0;
    width: 573px; height: 916px;
    background:
      radial-gradient(ellipse at 75% 65%, rgba(170,30,30,0.55), transparent 30%),
      radial-gradient(ellipse at 85% 60%, rgba(150,190,110,0.45), transparent 45%),
      linear-gradient(200deg, var(--forest-mid) 0%, var(--forest-deep) 40%, var(--forest-mid) 75%, var(--forest-deep) 100%);
  }
  .spine {
    position: absolute;
    left: 573px; top: 0;
    width: 54px; height: 916px;
    background: var(--spine-red);
  }
  .spine-author {
    position: absolute;
    left: 0; top: 76px;
    width: 54px;
    writing-mode: vertical-rl;
    text-align: left;
    color: var(--text-cream);
    font-size: 21px;
    letter-spacing: 7px;
    line-height: 54px;
  }
  .spine-title {
    position: absolute;
    left: 0; top: 376px;
    width: 54px;
    writing-mode: vertical-rl;
    color: var(--title-blue);
    font-style: italic;
    font-weight: 700;
    font-size: 40px;
    line-height: 54px;
    white-space: nowrap;
  }
  .synopsis {
    position: absolute;
    left: 60px; top: 112px;
    width: 456px;
    text-align: center;
    color: var(--text-cream);
    font-style: italic;
  }
  .synopsis-heading {
    margin: 0 0 22px;
    font-size: 16px;
    font-weight: 700;
    letter-spacing: 3px;
  }
  .synopsis-body {
    margin: 0;
    font-size: 15px;
    line-height: 20.7px;
    letter-spacing: 2.4px;
  }
  .isbn-box {
    position: absolute;
    left: 333px; top: 772px;
    width: 201px; height: 107px;
    background: var(--box-white);
  }
  .front-title {
    position: absolute;
    left: 688px; top: 10px;
    margin: 0;
    font-weight: 400;
    font-style: italic;
    line-height: 1;
  }
  .front-title .title-small {
    display: block;
    color: var(--title-blue);
    font-size: 58px;
    margin-left: 14px;
    letter-spacing: -1px;
  }
  .front-title .title-large {
    display: block;
    color: var(--title-white);
    font-size: 128px;
    letter-spacing: -4px;
    line-height: 0.82;
  }
  .front-title .title-large.second {
    margin-left: 70px;
  }
  .front-author {
    position: absolute;
    left: 734px; top: 851px;
    color: var(--title-blue);
    font-size: 27px;
    letter-spacing: 12.5px;
    margin: 0;
  }
</style>
</head>
<body>
<main class="cover-wrap">
  <div class="back-photo" role="img" aria-label="Shaded forest with a large oak trunk and green leaves"></div>
  <div class="front-photo" role="img" aria-label="Young woman with long dark hair in a long red dress leaning against a large oak tree in a forest"></div>

  <section class="synopsis">
    <h2 class="synopsis-heading">SYNOPSIS OF THE BOOK HERE</h2>
    <p class="synopsis-body">Synopsis of the book here Synopsis of the book here Synopsis of the book here Synopsis of the book here Synopsis of the book here Synopsis of the book here Synopsis of the book here Synopsis of the book here Synopsis of the book here Synopsis of the book here Synopsis of the book here Synopsis of the book here</p>
  </section>
  <div class="isbn-box"></div>

  <aside class="spine">
    <div class="spine-author">AUTHOR NAME</div>
    <div class="spine-title">Under Birch light</div>
  </aside>

  <h1 class="front-title">
    <span class="title-small">UNDER</span>
    <span class="title-large">BIRCH</span>
    <span class="title-large second">LIGHT</span>
  </h1>
  <p class="front-author">AUTHOR NAME</p>
</main>
</body>
</html>
```